Apartment Investor Business Card Design

Need a new business card designed for my multifamily investment company

Industry/Entity Type

Real Estate

Contact Information for Business Card

Garrick Pelham - President & CEO
Brightwold Holdings, LLC
4838 North 92nd Avenue, Ste 500
Omaha, NE 68999
(402) 555-0147
Garrick@brightwoldholdings.example
Www.BrightwoldHoldings.example

Colors
3176b5

```html
<!DOCTYPE html>
<html lang="en">
<head>
<meta charset="utf-8">
<title>Brightwold Holdings – Business Card</title>
<link rel="stylesheet" href="https://fonts.googleapis.com/css2?family=Cinzel:wght@400;700&family=Questrial&display=swap">
<style>
  :root {
    --page-bg: #d9d9d9;
    --charcoal: #2f2f2f;
    --charcoal-light: #555555;
    --navy: #29446f;
    --navy-deep: #223a62;
    --steel-blue: #4a72a6;
    --brand-blue: #3176b5;
    --white: #ffffff;
  }
  * { box-sizing: border-box; margin: 0; padding: 0; }
  html, body { width: 960px; height: 1200px; overflow: hidden; }
  body { background: var(--page-bg); position: relative; }

  .card {
    position: absolute;
    width: 736px;
    height: 441px;
    overflow: hidden;
    background: var(--charcoal);
  }
  .card--front { left: 114px; top: 85px; }
  .card--back  { left: 113px; top: 673px; }

  .card__art { position: absolute; inset: 0; width: 100%; height: 100%; }

  .brand-name {
    position: absolute;
    font-family: "Cinzel", serif;
    font-weight: 400;
    color: var(--white);
    white-space: nowrap;
    transform: translateX(-50%);
    letter-spacing: 0.02em;
  }
  .card--front .brand-name { left: 368px; top: 250px; font-size: 31px; }
  .card--back .brand-name  { left: 156px; top: 378px; font-size: 21px; }

  .holder {
    position: absolute;
    right: 33px;
    top: 24px;
    text-align: right;
  }
  .holder__name {
    font-family: "Cinzel", serif;
    font-weight: 700;
    font-size: 25px;
    letter-spacing: 0.08em;
    color: var(--white);
    line-height: 1.1;
  }
  .holder__title {
    font-family: "Questrial", sans-serif;
    font-size: 15px;
    letter-spacing: 0.14em;
    color: var(--brand-blue);
    line-height: 1.2;
  }
  .holder__rule {
    position: absolute;
    left: 362px;
    top: 74px;
    width: 341px;
    height: 3px;
    background: var(--brand-blue);
  }

  .contact-list { list-style: none; }
  .contact {
    position: absolute;
    left: 342px;
    display: flex;
    align-items: center;
    font-family: "Questrial", sans-serif;
    font-size: 17px;
    line-height: 1.05;
    color: var(--white);
  }
  .contact__icon { width: 33px; height: 33px; flex: none; margin-right: 6px; }
  .contact--address { top: 83px; }
  .contact--phone   { top: 143px; }
  .contact--email   { top: 197px; }
  .contact--web     { top: 249px; }
</style>
</head>
<body>

<section class="card card--front" aria-label="Business card front">
  <svg class="card__art" viewBox="0 0 919 551" preserveAspectRatio="none" aria-hidden="true">
    <defs>
      <radialGradient id="front-glow" cx="0.5" cy="0.48" r="0.55">
        <stop offset="0" stop-color="#5a5a5a"/>
        <stop offset="1" stop-color="#2e2e2e"/>
      </radialGradient>
    </defs>
    <rect width="919" height="551" fill="url(#front-glow)"/>
    <path d="M0,70 C60,260 200,470 340,500 C440,522 520,540 580,551 L0,551 Z" fill="#29446f"/>
    <path d="M0,70 C70,280 230,460 340,500 C220,470 80,360 0,250 Z" fill="#3a5f95"/>
    <path d="M520,0 C700,80 840,260 919,430 L919,0 Z" fill="#2a4575"/>
    <path d="M520,0 C660,60 790,190 880,360 C800,170 720,70 700,0 Z" fill="#4a70a0"/>
  </svg>
  <p class="brand-name">Brightwold Holdings</p>
</section>

<section class="card card--back" aria-label="Business card back">
  <svg class="card__art" viewBox="0 0 919 551" preserveAspectRatio="none" aria-hidden="true">
    <defs>
      <radialGradient id="back-glow" cx="0.45" cy="0.3" r="0.6">
        <stop offset="0" stop-color="#565656"/>
        <stop offset="1" stop-color="#2e2e2e"/>
      </radialGradient>
    </defs>
    <rect width="919" height="551" fill="url(#back-glow)"/>
    <path d="M0,110 C220,280 520,430 919,545 L919,551 L0,551 Z" fill="#3a5f95"/>
    <path d="M0,150 C220,320 520,450 919,551 L0,551 Z" fill="#29446f"/>
  </svg>

  <p class="brand-name">Brightwold Holdings</p>

  <header class="holder">
    <h1 class="holder__name">GARRICK PELHAM</h1>
    <p class="holder__title">PRESIDENT &amp; CEO</p>
  </header>
  <div class="holder__rule"></div>

  <ul class="contact-list">
    <li class="contact contact--address">
      <svg class="contact__icon" viewBox="0 0 32 32" aria-hidden="true">
        <circle cx="16" cy="16" r="16" fill="#3176b5"/>
        <path d="M9,16 L16,9.5 L23,16 M11,14.5 V22.5 H21 V14.5 M14.5,22.5 V18 H17.5 V22.5" fill="none" stroke="#fff" stroke-width="1.4" stroke-linejoin="round"/>
      </svg>
      <span>Brightwold Holdings, LLC<br>4838 North 92nd Avenue, Ste 500<br>Omaha, NE 68999</span>
    </li>
    <li class="contact contact--phone">
      <svg class="contact__icon" viewBox="0 0 32 32" aria-hidden="true">
        <circle cx="16" cy="16" r="16" fill="#3176b5"/>
        <path d="M10.5,9 L13.5,9 L14.5,12.5 L12.8,14 C13.8,16.3 15.7,18.2 18,19.2 L19.5,17.5 L23,18.5 L23,21.5 C23,22.3 22.3,23 21.5,23 C15,22.5 9.5,17 9,10.5 C9,9.7 9.7,9 10.5,9 Z" fill="none" stroke="#fff" stroke-width="1.4" stroke-linejoin="round"/>
      </svg>
      <span>(402) 555-0147</span>
    </li>
    <li class="contact contact--email">
      <svg class="contact__icon" viewBox="0 0 32 32" aria-hidden="true">
        <circle cx="16" cy="16" r="16" fill="#3176b5"/>
        <rect x="8.5" y="11" width="15" height="10.5" fill="none" stroke="#fff" stroke-width="1.4"/>
        <path d="M8.5,11 L16,17 L23.5,11" fill="none" stroke="#fff" stroke-width="1.4"/>
      </svg>
      <span>Garrick@brightwoldholdings.example</span>
    </li>
    <li class="contact contact--web">
      <svg class="contact__icon" viewBox="0 0 32 32" aria-hidden="true">
        <circle cx="16" cy="16" r="16" fill="#3176b5"/>
        <g fill="none" stroke="#fff" stroke-width="1.3">
          <circle cx="16" cy="16" r="7.5"/>
          <ellipse cx="16" cy="16" rx="3.3" ry="7.5"/>
          <path d="M8.5,16 H23.5 M9.5,12.3 H22.5 M9.5,19.7 H22.5"/>
        </g>
      </svg>
      <span>www.BrightwoldHoldings.example</span>
    </li>
  </ul>
</section>

</body>
</html>
```